依頼概要
■依頼の目的/概要
弊社で販売を予定している自然食品(アマランサス)のラベルデザインをお願いします。

■依頼詳細
話題のスーパーグレイン(脅威の穀物)、アマランサスのラベルデザインです。
チャック付きのアルミ袋に貼るラベルのデザインをお願いいたします。

■サイズ
ラベルサイズは 100mm×100mm で設定してください。

ラベルを貼付するアルミ袋(パクロンBX-27)のサイズは下記のとおりです。

チャック下 200mm×袋巾 140mm + 底ガゼット 41mm

■記載必須の文言
商品名:Amaranthus (小文字・大文字は問いません)、アマランサス

※商品名は英語、日本語のいずれか、または両方でも構いません。

※上記以外の文言は任意です。

■商品詳細
原材料:アマランサス
原産国:インド(原産国は変更になる場合があります)

商品説明:
タンパク質や鉄、カルシウム、マグネシウム、食物繊維などが豊富なスーパーグレイン(脅威の穀物)。
偏りがちな現代人の食生活を補完する食品として最適です。
アマランサスは、古代インカ文明ではトウモロコシや豆類に匹敵する貴重な作物だったと伝えられています。
19世紀に入るとインドなどでも大規模に栽培され、日本には江戸時代に伝来しました。
お米に混ぜて炊いたり、手作りのパンに混ぜることで米や小麦粉の栄養価を高めることができます。
また、サラダのトッピングや和え物としてもご使用いただけます。

■画像
ご参考までに1点、画像素材を添付いたします。こちらの利用は任意です。

その他何かご不明な点がございましたら、ご遠慮なくお問い合わせください。
よろしくお願いいたします。
■ 選んだ理由

アマランサスの花をモチーフとした文様がシンプルで美しく、飽きのこないデザインだと思いました。

■ 提案者全員のお礼・コメント

たくさんの魅力的なご提案をいただき、ありがとうございました。次回新製品投入の際にもまたこちらのサイトを利用したいと思います。

```html
<!DOCTYPE html>
<html lang="ja">
<head>
<meta charset="utf-8">
<title>アマランサス ラベル</title>
<link rel="stylesheet" href="https://fonts.googleapis.com/css2?family=Noto+Sans+JP:wght@500;700;900&family=Playfair+Display:wght@700;900&display=swap">
<style>
  :root {
    --page: #eceef0;
    --label-yellow: #ffe93a;
    --label-green: #cfe9a6;
    --deep-green: #1f8a2c;
    --headline-red: #d8141b;
    --arc-orange: #ef7a10;
    --ink: #1a1a1a;
    --paper: #ffffff;
    --grain-light: #e6d49a;
    --grain-dark: #b89a52;
  }
  * { box-sizing: border-box; margin: 0; padding: 0; }
  html, body {
    width: 833px; height: 1200px; overflow: hidden;
    background: var(--page);
    font-family: "Noto Sans JP", sans-serif;
  }
  .label {
    position: absolute; left: 46px; top: 230px;
    width: 740px; height: 740px;
    background: var(--paper);
    border: 3px solid var(--headline-red);
    overflow: hidden;
  }
  .label__headline {
    height: 86px;
    background: var(--label-yellow);
    display: flex; align-items: center; justify-content: center;
    font-weight: 900; font-size: 46px; letter-spacing: 1px;
    color: var(--headline-red);
    border-bottom: 3px solid var(--headline-red);
  }
  .label__hero {
    position: relative; height: 400px;
    background: linear-gradient(180deg, var(--label-green), #eaf6c9);
  }
  .hero__arc { position: absolute; left: 0; top: 0; width: 734px; height: 400px; z-index: 2; }
  .hero__arc text {
    font-family: "Noto Sans JP", sans-serif; font-weight: 900;
    fill: var(--arc-orange); stroke: var(--paper); stroke-width: 5px;
    paint-order: stroke;
  }
  .hero__grains {
    position: absolute; left: 250px; top: 40px;
    width: 240px; height: 185px; border-radius: 50%;
    background: radial-gradient(circle at 45% 40%, var(--grain-light), var(--grain-dark));
  }
  .hero__origin {
    position: absolute; left: 270px; top: 205px;
    font-size: 22px; font-weight: 700; color: var(--ink);
    background: var(--paper); padding: 0 6px;
  }
  .hero__latin {
    position: absolute; left: 0; right: 0; top: 228px; text-align: center;
    font-family: "Playfair Display", serif; font-weight: 900;
    font-size: 74px; color: var(--ink); line-height: 1;
  }
  .hero__kana {
    position: absolute; left: 0; right: 0; top: 305px; text-align: center;
    font-weight: 900; font-size: 76px; line-height: 1;
    color: var(--deep-green);
    -webkit-text-stroke: 2px var(--paper);
    text-shadow: 0 0 4px var(--paper), 0 0 4px var(--paper);
  }
  .label__description {
    padding: 22px 30px;
    font-size: 19px; font-weight: 500; line-height: 1.6;
    color: var(--ink);
    border-top: 3px solid var(--deep-green);
  }
  .label__description p + p { margin-top: 6px; }
  .label__description .accent { color: var(--headline-red); font-weight: 700; }
</style>
</head>
<body>
  <section class="label">
    <header class="label__headline">偏りがちな現代人の食生活に</header>
    <div class="label__hero">
      <div class="hero__grains" role="img" aria-label="アマランサスの穀粒の写真"></div>
      <svg class="hero__arc" viewBox="0 0 734 400" aria-hidden="true">
        <defs>
          <path id="arc-outer" d="M28 335 Q 110 20 715 40"/>
          <path id="arc-inner" d="M88 335 Q 170 85 600 80"/>
        </defs>
        <text font-size="24"><textPath href="#arc-outer">タンパク質や鉄、カルシウム、マグネシウム、食物繊維など</textPath></text>
        <text font-size="24"><textPath href="#arc-inner">スーパーグレイン（脅威の穀物）が豊富</textPath></text>
      </svg>
      <div class="hero__origin">原産国：インド</div>
      <div class="hero__latin">Amaranthus</div>
      <div class="hero__kana">アマランサス</div>
    </div>
    <div class="label__description">
      <p>アマランサスは、古代インカ文明ではトウモロコシや豆類に匹敵する貴重な作物だったと伝えられています。19世紀に入るとインドなどでも大規模に栽培され、日本には江戸時代に伝来しました。</p>
      <p>お米に混ぜて炊いたり、手作りのパンに混ぜることで米や小麦粉の栄養価を高めることができます。また、サラダのトッピングや和え物としてもご使用いただけます。<span class="accent">偏りがちな現代人の食生活を補完する食品として最適です。</span></p>
    </div>
  </section>
</body>
</html>
```